Business Card and Letterhead for new company Vardel GreenWorks, Inc.

Vardel GreenWorks, Inc., an engineering and construction firm that provides services for solid waste landfill gas systems, needs a business card and letterhead. We recently had a logo designed but we are open to some tweaks to logo design and color scheme. Generally, we like "earthy" color tones - greens, browns, oranges. This is a sister company - www.talvoriengineering.example.

Target Market(s)

Solid waste landfill companies - Brindle Disposal, Halcott Hauling, etc.

Industry/Entity Type

Engineering and Construction

Contact Information for Business Card

Name, Title, email, mobile phone, work phone, website. Potential list of services for back of card: LFG Engineering and Design, GCCS Planning and Operational Consulting, Compliance Monitoring and Reporting, Routine Operations & Maintenance, Nonroutine O&M, Construction Management, Construction QA, GCCS Construction

Font styles to use
Sans Serif

Requirements
Must have
• Logo, pertinent information, maybe a tagline (still in development)
Nice to have
• For back of card, considering an engineering scale (attached for another business of ours), but want to look at other options, alternatives. Like the idea of the back of card to have some utility (scale, unit conversion info, list of services) but willing to consider lots of options.
Should not have
• Needs to have a professional (engineering) and technical look, not cartoonish.

```html
<!DOCTYPE html>
<html lang="en">
<head>
<meta charset="utf-8">
<title>Vardel GreenWorks – Business Card</title>
<link href="https://fonts.googleapis.com/css2?family=Lato:wght@400;700&display=swap" rel="stylesheet">
<style>
  :root {
    --stage: #78b545;
    --card: #ffffff;
    --band: #050608;
    --green: #6db33f;
    --grey: #8a8a8a;
    --ink: #1d1d1f;
    --icon: #5a5f66;
    --faint: #f3f4f6;
  }
  * { margin: 0; padding: 0; box-sizing: border-box; }
  html, body { width: 1200px; height: 996px; overflow: hidden; }
  body { background: var(--stage); font-family: "Lato", sans-serif; position: relative; }

  .card {
    position: absolute; left: 332px; width: 537px; height: 305px;
    background: var(--card); border-radius: 23px; overflow: hidden;
  }
  .card--front { top: 177px; }
  .card--back { top: 513px; }

  .front-band {
    position: absolute; left: 0; top: 0; width: 100%; height: 120px;
    background: var(--band); border-bottom: 1px solid var(--green);
  }
  .brand {
    position: absolute; display: flex; align-items: center; gap: 10px;
    color: var(--green); font-weight: 700; white-space: nowrap;
  }
  .brand__dot { border-radius: 50%; background: var(--green); flex: none; }
  .card--front .brand { left: 22px; top: 42px; font-size: 22px; }
  .card--front .brand__dot { width: 34px; height: 34px; }

  .front-accent {
    position: absolute; left: 394px; top: 72px; width: 118px; height: 118px;
    border-radius: 50%; background: var(--green);
    border: 4px solid var(--card);
  }

  .person { position: absolute; left: 23px; top: 156px; }
  .person__name { color: var(--green); font-size: 23px; font-weight: 700; line-height: 1.1; }
  .person__title { color: var(--grey); font-size: 16.5px; line-height: 1.3; }

  .contacts { position: absolute; top: 226px; list-style: none; }
  .contacts--phones { left: 24px; }
  .contacts--web { left: 285px; }
  .contacts li {
    display: flex; align-items: center; gap: 12px;
    font-size: 15.5px; color: var(--ink); height: 24.5px; white-space: nowrap;
  }
  .contacts svg { width: 14px; height: 14px; fill: var(--icon); flex: none; }

  .back-mark {
    position: absolute; left: 340px; top: 40px; width: 170px; height: 230px;
    border-radius: 50%; background: var(--faint);
  }
  .card--back .brand { left: 50%; top: 130px; transform: translateX(-50%); font-size: 28px; }
  .card--back .brand__dot { width: 42px; height: 42px; }
  .back-url {
    position: absolute; left: 0; width: 100%; top: 253px;
    text-align: center; font-size: 15px; color: var(--ink);
  }
</style>
</head>
<body>

<section class="card card--front">
  <div class="front-band"></div>
  <div class="brand"><span class="brand__dot"></span>Vardel GreenWorks</div>
  <div class="front-accent"></div>

  <div class="person">
    <p class="person__name">Owen Castellan</p>
    <p class="person__title">General Manager</p>
  </div>

  <ul class="contacts contacts--phones">
    <li><svg viewBox="0 0 24 24"><path d="M6.6 10.8a15.1 15.1 0 0 0 6.6 6.6l2.2-2.2c.3-.3.7-.4 1-.2 1.1.4 2.3.6 3.6.6.6 0 1 .4 1 1V20c0 .6-.4 1-1 1A17 17 0 0 1 3 4c0-.6.4-1 1-1h3.5c.6 0 1 .4 1 1 0 1.3.2 2.5.6 3.6.1.3 0 .7-.2 1z"/></svg>+1 (555) 014 2231</li>
    <li><svg viewBox="0 0 24 24"><path d="M6.6 10.8a15.1 15.1 0 0 0 6.6 6.6l2.2-2.2c.3-.3.7-.4 1-.2 1.1.4 2.3.6 3.6.6.6 0 1 .4 1 1V20c0 .6-.4 1-1 1A17 17 0 0 1 3 4c0-.6.4-1 1-1h3.5c.6 0 1 .4 1 1 0 1.3.2 2.5.6 3.6.1.3 0 .7-.2 1z"/></svg>+1 (555) 018 6470</li>
  </ul>

  <ul class="contacts contacts--web">
    <li><svg viewBox="0 0 24 24"><path d="M3 5h18v14H3zm2 2v.5l7 4.5 7-4.5V7l-7 4.5z"/></svg>info@vardel_gworks.example</li>
    <li><svg viewBox="0 0 24 24"><path d="M10 2a8 8 0 1 0 4.9 14.3l5.4 5.4 1.4-1.4-5.4-5.4A8 8 0 0 0 10 2zm0 2a6 6 0 1 1 0 12 6 6 0 0 1 0-12z"/></svg>www.vardelgworks.example</li>
  </ul>
</section>

<section class="card card--back">
  <div class="back-mark"></div>
  <div class="brand"><span class="brand__dot"></span>Vardel GreenWorks</div>
  <p class="back-url">www.vardelgworks.example</p>
</section>

</body>
</html>
```